Chocolate company needing sticker for products

I have a small chocolate company Willow Bend Sweets in Austin Texas. I make all vegan, gluten free, organic, faire trade chocolate that tastes amazing! It is allergy friendly approvable by all ages. I want to have a great sticker that i can put on our boxes and bags. I am using a lot of natural craft color and brown. I am open to color options possibly for different flavors. I want the packaging to reflect the basis of my company. It is all handmade by me but i don't want it to have to much of a crafty look to it. I have attached the logo designs I have. it the sticker can have som of the bullet points about the company that would be great. But it needs to say Locally Made in Austin Texas. it also has to have the company address.
418 West Cobbler Ridge Rd #207 Austin Tx 78745. These things are required by the state for food regulations. I want something that looks great and I can be really proud to put on my product! Thanks so much for all of your help in advance. Dot

I also need some other information added to the sticker. Website which is willowbendsweetsatx.com 

Phone number 512.368.4175. Instagram willowbendsweets. Thanks for your hard work! 

Industry/Entity Type

Chocolate Company

Requirements
Must have
• The logo is added at the bottom as well as designs I like I want to have a professional look but it to be approvable by all consumers. I will gig feed back as i see what designs come through. This will probably fold out into a multi design project so i will be looking for assistance on other areas of this as well. Thanks

```html
<!DOCTYPE html>
<html lang="en">
<head>
<meta charset="utf-8">
<title>Willow Bend Sweets – Product Stickers</title>
<link href="https://fonts.googleapis.com/css2?family=Questrial&family=Roboto:wght@400&display=swap" rel="stylesheet">
<style>
  :root {
    --page: #ffffff;
    --paper: #f3f2ea;
    --cocoa: #2a1a14;
    --mint: #b2f5e2;
    --mint-line: #a7efd9;
  }
  html, body {
    margin: 0;
    padding: 0;
    width: 1200px;
    height: 773px;
    overflow: hidden;
    background: var(--page);
  }
  .canvas {
    position: relative;
    width: 950px;
    height: 612px;
    transform: scale(1.2632);
    transform-origin: 0 0;
  }
  .sticker {
    position: absolute;
    left: 240px;
    width: 457px;
    height: 242px;
    background: var(--paper);
    color: var(--cocoa);
  }
  .sticker--crisps { top: 45px; }
  .sticker--caramels { top: 314px; }
  .sticker__frame {
    position: absolute;
    left: 6px; top: 6px;
    width: 442px; height: 226px;
    border: 1.5px solid var(--cocoa);
  }
  .sticker__origin {
    position: absolute;
    left: 10px; top: 12px;
    width: 437px;
    margin: 0;
    font-family: "Questrial", sans-serif;
    font-size: 27px;
    font-weight: 400;
    text-align: center;
    letter-spacing: 0.2px;
    white-space: nowrap;
    line-height: 1;
  }
  .sticker__rule {
    position: absolute;
    left: 12px; top: 44px;
    width: 433px; height: 3px;
    border-top: 1px solid var(--cocoa);
    border-bottom: 1px dotted var(--cocoa);
  }
  .brand-mark {
    position: absolute;
    left: 18px; top: 54px;
    width: 170px; height: 170px;
    box-sizing: border-box;
    display: flex;
    align-items: center;
    justify-content: center;
  }
  .brand-mark--mint {
    background: var(--mint);
    border: 3px solid var(--cocoa);
    box-shadow: inset 0 0 0 3px var(--mint), inset 0 0 0 4px var(--cocoa);
  }
  .brand-mark--cocoa {
    background: var(--cocoa);
    box-shadow: inset 0 0 0 5px var(--cocoa), inset 0 0 0 6px var(--mint);
  }
  .brand-mark__name {
    font-family: "Questrial", sans-serif;
    font-size: 28px;
    line-height: 1.08;
    text-align: center;
    text-transform: uppercase;
    color: var(--cocoa);
  }
  .brand-mark--cocoa .brand-mark__name { color: var(--mint); }
  .sticker__divider {
    position: absolute;
    left: 198px; top: 50px;
    width: 1px; height: 178px;
    background: var(--mint-line);
  }
  .details {
    position: absolute;
    left: 207px; top: 50px;
    width: 236px;
  }
  .details__line {
    height: 1px;
    background: var(--mint-line);
    position: absolute;
    left: 0; width: 236px;
  }
  .details__line--claims { top: 21px; }
  .details__line--product { top: 111px; }
  .details__line--web { top: 138px; }
  .details__line--contact { top: 160px; }
  .details__claims {
    position: absolute;
    top: 5px; left: 0;
    margin: 0;
    font-family: "Roboto", sans-serif;
    font-size: 9.8px;
    line-height: 1.2;
    white-space: nowrap;
  }
  .details__product {
    position: absolute;
    top: 27px; left: 0;
    margin: 0;
    font-family: "Questrial", sans-serif;
    font-weight: 400;
    font-size: 33px;
    line-height: 38px;
    letter-spacing: 1.4px;
    white-space: nowrap;
  }
  .sticker--caramels .details__product {
    font-size: 30px;
    letter-spacing: 0.8px;
    top: 30px;
  }
  .details__web {
    position: absolute;
    top: 116px; left: 0;
    margin: 0;
    font-family: "Questrial", sans-serif;
    font-size: 15.6px;
    line-height: 1.2;
    white-space: nowrap;
  }
  .details__contact {
    position: absolute;
    top: 143px; left: 0;
    margin: 0;
    display: flex;
    align-items: center;
    gap: 8px;
    font-family: "Roboto", sans-serif;
    font-size: 10.3px;
    line-height: 1.2;
    white-space: nowrap;
  }
  .details__dot {
    width: 7px; height: 7px;
    background: var(--mint);
    display: inline-block;
  }
  .details__address {
    position: absolute;
    top: 166px; left: 0;
    margin: 0;
    font-family: "Roboto", sans-serif;
    font-size: 9.8px;
    line-height: 1.2;
    white-space: nowrap;
  }
</style>
</head>
<body>
<div class="canvas">

  <section class="sticker sticker--crisps">
    <div class="sticker__frame"></div>
    <h1 class="sticker__origin">LOCALLY MADE IN AUSTIN, TEXAS</h1>
    <div class="sticker__rule"></div>
    <div class="brand-mark brand-mark--mint">
      <div class="brand-mark__name">Willow<br>Bend<br>Sweets</div>
    </div>
    <div class="sticker__divider"></div>
    <div class="details">
      <p class="details__claims">Vegan, Gluten Free, Organic, Fair Trade Chocolates</p>
      <div class="details__line details__line--claims"></div>
      <h2 class="details__product">CHOCOLATE &amp;<br>RICE CRISPS</h2>
      <div class="details__line details__line--product"></div>
      <p class="details__web">WILLOWBENDSWEETSATX.COM</p>
      <div class="details__line details__line--web"></div>
      <p class="details__contact">512.368.4175 <span class="details__dot"></span> Instagram: willowbendsweets</p>
      <div class="details__line details__line--contact"></div>
      <p class="details__address">418 West Cobbler Ridge Rd #207 Austin Tx 78745</p>
    </div>
  </section>

  <section class="sticker sticker--caramels">
    <div class="sticker__frame"></div>
    <h1 class="sticker__origin">LOCALLY MADE IN AUSTIN, TEXAS</h1>
    <div class="sticker__rule"></div>
    <div class="brand-mark brand-mark--cocoa">
      <div class="brand-mark__name">Willow<br>Bend<br>Sweets</div>
    </div>
    <div class="sticker__divider"></div>
    <div class="details">
      <p class="details__claims">Vegan, Gluten Free, Organic, Fair Trade Chocolates</p>
      <div class="details__line details__line--claims"></div>
      <h2 class="details__product">DARK SEA SALT<br>CARAMEL BITES</h2>
      <div class="details__line details__line--product"></div>
      <p class="details__web">WILLOWBENDSWEETSATX.COM</p>
      <div class="details__line details__line--web"></div>
      <p class="details__contact">512.368.4175 <span class="details__dot"></span> Instagram: willowbendsweets</p>
      <div class="details__line details__line--contact"></div>
      <p class="details__address">418 West Cobbler Ridge Rd #207 Austin Tx 78745</p>
    </div>
  </section>

</div>
</body>
</html>
```